Landscape Supplier and Excavation company needing a website revamp.

We need a web design for our company based out of northern Virginia. We make and deliver topsoil, mulch, and compost. We are also an excavation company. We provide a wide variety of excavation services, from residential to large commercial projects. We specialize in land clearing and building site preparation. We would like a site that looks very professional and makes us look like a large company. We've been in business since 1994 and have never had a really nice website. Our current website it www.hollowbrookloam.com and www.rkqmo.com for references. I like the information on the pages but would like something more professional looking. Doesn't HAVE to be 4 different pages, but I would like a contact form, our services, and our products/ pricing listed. We are properly licensed and insured and would like this included somewhere on the site.

Target Market(s)

Landscapers, Home Owners, Commercial

Industry/Entity Type

Excavation and Landscape Products Supplier

Number of Pages Required

4 page

Colors

Designer to choose colors to be used in the design.

Requirements
Must have
• Professional Look and Feel

```html
<!DOCTYPE html>
<html lang="en">
<head>
<meta charset="utf-8">
<title>Hollowbrook Loam – Responsive Website</title>
<link rel="stylesheet" href="https://fonts.googleapis.com/css2?family=Poppins:wght@400;600;700;800&display=swap">
<style>
:root{
  --red:#b5121b;
  --red-deep:#7d0b10;
  --red-soft:#d43a3f;
  --ink:#1d1d1f;
  --char:#2a2a2c;
  --grey:#6b6b6b;
  --line:#e2e2e2;
  --paper:#ffffff;
  --board:#f4f4f4;
}
*{box-sizing:border-box;margin:0;padding:0}
html,body{width:720px;height:1200px;overflow:hidden}
body{background:var(--paper);font-family:"Poppins",Arial,sans-serif;color:var(--ink);position:relative}

.device-icon{position:absolute;top:30px}
.screen{position:absolute;top:96px;background:var(--paper);box-shadow:0 2px 10px rgba(0,0,0,.18);display:flex;flex-direction:column;overflow:hidden}
.screen--desktop{left:22px;width:314px;height:1084px}
.screen--tablet{left:358px;width:232px;height:1084px}
.screen--mobile{left:604px;width:94px;height:1084px}

.nav{display:flex;align-items:center;justify-content:space-between;background:var(--paper);padding:0 8px;flex:none}
.brand{color:var(--red);font-weight:800;text-transform:uppercase;line-height:1;display:flex;align-items:center;gap:3px;white-space:nowrap}
.brand__dot{width:6px;height:6px;border-radius:50%;background:var(--red)}
.nav__links{display:flex;gap:7px;font-size:4.5px;color:var(--ink)}
.btn{display:inline-block;background:var(--red);color:#fff;font-weight:600;border-radius:2px;line-height:1;white-space:nowrap}

.hero{position:relative;flex:none;background:linear-gradient(135deg,#3d3a2f 0%,#1f2a1b 45%,#2b1e16 100%);color:#fff;display:flex;flex-direction:column;justify-content:center}
.hero::after{content:"";position:absolute;inset:0;background:linear-gradient(90deg,rgba(0,0,0,.55),rgba(0,0,0,.1))}
.hero__body{position:relative;z-index:1}
.hero__eyebrow{font-size:4.5px;color:#ddd;margin-bottom:3px}
.hero__title{font-weight:700;line-height:1.2}

.features{display:flex;justify-content:space-around;align-items:center;flex:none;background:var(--paper);border-bottom:1px solid var(--line)}
.feature{display:flex;flex-direction:column;align-items:center;gap:2px;font-size:4px;color:var(--ink)}
.feature__icon{border-radius:50%;background:var(--red);display:flex;align-items:center;justify-content:center}

.section-label{font-size:4px;color:var(--red);font-weight:600;text-transform:uppercase}
.heading{font-weight:700;color:var(--ink);line-height:1.2}
.heading--light{color:#fff}
.text{font-size:4.3px;color:var(--grey);line-height:1.5}
.photo{border-radius:2px}
.photo--garden{background:linear-gradient(135deg,#6f8a3d,#3a4d22 60%,#8a2a22)}
.photo--soil{background:linear-gradient(135deg,#6b4a32,#3a2a1e)}
.photo--machine{background:linear-gradient(135deg,#8b7a55,#4a4536 60%,#2b2b26)}
.photo--forest{background:linear-gradient(160deg,#25361f,#3f5a30 50%,#1b2616)}

.welcome{display:flex;align-items:center;flex:none;background:var(--paper)}
.services{flex:none;background:var(--board);text-align:center}
.service-grid{display:flex;justify-content:center}
.service-card{background:var(--char);color:#fff;border-radius:2px;overflow:hidden;text-align:left}
.service-card__title{font-weight:600}
.service-btn{font-size:4px;padding:3px 0;width:100%;text-align:center;margin-top:3px}

.calc{flex:none;background:radial-gradient(circle at 30% 20%,var(--red-soft),var(--red) 40%,var(--red-deep));text-align:center;display:flex;flex-direction:column;align-items:center}
.calc__panel{background:var(--char);border-radius:3px;display:flex;flex-direction:column;text-align:left}
.calc__row{display:flex;align-items:center;justify-content:space-between;border-bottom:1px solid #3d3d40;color:#ddd;font-size:4.3px}
.calc__field{background:#3a3a3d;border-radius:1px}
.calc__tick{color:#6dbb4a;font-size:5px}

.reviews{flex:none;background:var(--paper);text-align:center;display:flex;flex-direction:column;align-items:center}
.review{display:flex;align-items:center}
.review__avatar{border-radius:50%;background:linear-gradient(135deg,#9a8a78,#5a4b3e);flex:none}
.review__quote{border:1px solid var(--red);border-radius:3px;text-align:left}

.contact{flex:none;position:relative;display:flex;flex-direction:column;align-items:center;justify-content:center}
.contact__card{display:flex;background:var(--char);border-radius:3px;overflow:hidden;position:relative;z-index:1}
.contact__info{background:var(--red);color:#fff}
.contact__map{background:linear-gradient(135deg,#e9e6df,#d6d9cf);flex:1}
.contact__form{position:relative;z-index:1;background:var(--ink);display:flex;align-items:center}
.input{background:#fff;border-radius:1px}

.footer{flex:1;background:radial-gradient(circle at 70% 0%,var(--red),var(--red-deep) 70%);color:#fff;display:flex;flex-direction:column}
.footer__cols{display:flex;flex:1}
.footer__col h4{font-size:5px;font-weight:600;margin-bottom:3px}
.footer__col p{font-size:4px;color:#f3d6d6;line-height:1.6}
.footer__base{background:rgba(0,0,0,.35);font-size:4px;text-align:center;color:#f0c9c9}
</style>
</head>
<body>

<svg class="device-icon" style="left:166px" width="30" height="26" viewBox="0 0 30 26" aria-hidden="true"><rect x="1" y="1" width="28" height="18" rx="1.5" fill="none" stroke="#222" stroke-width="2"/><rect x="12" y="19" width="6" height="4" fill="#222"/><rect x="8" y="23" width="14" height="2" fill="#222"/></svg>
<svg class="device-icon" style="left:464px" width="20" height="28" viewBox="0 0 20 28" aria-hidden="true"><rect x="1" y="1" width="18" height="26" rx="2" fill="none" stroke="#222" stroke-width="2"/><circle cx="10" cy="23" r="1.3" fill="#222"/></svg>
<svg class="device-icon" style="left:643px" width="14" height="26" viewBox="0 0 14 26" aria-hidden="true"><rect x="1" y="1" width="12" height="24" rx="2" fill="none" stroke="#222" stroke-width="2"/><circle cx="7" cy="21.5" r="1.1" fill="#222"/></svg>

<!-- ===== DESKTOP ===== -->
<main class="screen screen--desktop">
  <header class="nav" style="height:20px">
    <span class="brand" style="font-size:6px"><span class="brand__dot"></span>Hollowbrook Loam</span>
    <nav class="nav__links"><span>Home</span><span>About</span><span>Services</span><span>Products</span><span>Contact</span></nav>
    <span class="btn" style="font-size:4.5px;padding:3px 5px">Get A Quote</span>
  </header>

  <section class="hero" style="height:172px;padding:0 28px" role="img" aria-label="Photo of fresh topsoil and young plants in garden beds">
    <div class="hero__body">
      <p class="hero__eyebrow">Welcome To Hollowbrook Loam</p>
      <h1 class="hero__title" style="font-size:13px;width:150px">Providing Quality Topsoil And Mulch Since 1988</h1>
      <span class="btn" style="font-size:4.5px;padding:3px 6px;margin-top:6px">Read More</span>
    </div>
  </section>

  <section class="features" style="height:36px;padding:0 10px">
    <div class="feature"><span class="feature__icon" style="width:13px;height:13px"></span>Topsoil</div>
    <div class="feature"><span class="feature__icon" style="width:13px;height:13px"></span>Mulch</div>
    <div class="feature"><span class="feature__icon" style="width:13px;height:13px"></span>Compost</div>
    <div class="feature"><span class="feature__icon" style="width:13px;height:13px"></span>Excavation</div>
    <div class="feature"><span class="feature__icon" style="width:13px;height:13px"></span>Clearing</div>
    <div class="feature"><span class="feature__icon" style="width:13px;height:13px"></span>Delivery</div>
  </section>

  <section class="welcome" style="height:108px;padding:0 24px;gap:18px">
    <div style="flex:1">
      <p class="section-label">About Us</p>
      <h2 class="heading" style="font-size:9px;margin:2px 0 4px">Welcome To Hollowbrook Loam</h2>
      <p class="text">Family owned for decades, we make and deliver topsoil, mulch and compost across the region.</p>
      <span class="btn" style="font-size:4.5px;padding:3px 6px;margin-top:5px">Read More</span>
    </div>
    <div class="photo photo--garden" style="width:120px;height:74px" role="img" aria-label="Photo of hands holding rich dark soil"></div>
  </section>

  <section class="services" style="height:132px;padding:14px 16px 0">
    <p class="section-label">Our Services</p>
    <h2 class="heading" style="font-size:9px;margin-bottom:8px">How We Serve You</h2>
    <div class="service-grid" style="gap:6px">
      <article class="service-card" style="width:66px">
        <div class="photo--machine" style="height:40px" role="img" aria-label="Photo of an excavator on a job site"></div>
        <div style="padding:4px"><p class="service-card__title" style="font-size:5px">Excavation</p><p style="font-size:3.8px;color:#ccc;line-height:1.4">Site work for homes and large builds.</p></div>
      </article>
      <article class="service-card" style="width:66px">
        <div class="photo--soil" style="height:40px" role="img" aria-label="Photo of a pile of screened topsoil"></div>
        <div style="padding:4px"><p class="service-card__title" style="font-size:5px">Topsoil</p><p style="font-size:3.8px;color:#ccc;line-height:1.4">Screened soil made and delivered daily.</p></div>
      </article>
      <article class="service-card" style="width:66px">
        <div class="photo--forest" style="height:40px" role="img" aria-label="Photo of land being cleared of trees"></div>
        <div style="padding:4px"><p class="service-card__title" style="font-size:5px">Clearing</p><p style="font-size:3.8px;color:#ccc;line-height:1.4">Lot and land clearing of any size.</p></div>
      </article>
      <article class="service-card" style="width:66px">
        <div class="photo--machine" style="height:40px" role="img" aria-label="Photo of a grader leveling a building site"></div>
        <div style="padding:4px"><p class="service-card__title" style="font-size:5px">Grading</p><p style="font-size:3.8px;color:#ccc;line-height:1.4">Building pad and site preparation.</p></div>
      </article>
    </div>
  </section>

  <section class="calc" style="height:228px;padding-top:16px">
    <p class="section-label" style="color:#fbd">Calculator</p>
    <h2 class="heading heading--light" style="font-size:9px;margin-bottom:10px">How Much Do I Need?</h2>
    <div class="calc__panel" style="width:230px;padding:10px 12px;gap:2px">
      <div class="calc__row" style="height:22px"><span>Material</span><span class="calc__field" style="width:110px;height:9px"></span><span class="calc__tick">✓</span></div>
      <div class="calc__row" style="height:22px"><span>Length (ft)</span><span class="calc__field" style="width:110px;height:9px"></span><span class="calc__tick">✓</span></div>
      <div class="calc__row" style="height:22px"><span>Width (ft)</span><span class="calc__field" style="width:110px;height:9px"></span><span class="calc__tick">✓</span></div>
      <div class="calc__row" style="height:22px"><span>Depth (in)</span><span class="calc__field" style="width:110px;height:9px"></span><span class="calc__tick">✓</span></div>
      <div class="calc__row" style="height:22px"><span>Cubic Yards</span><span class="calc__field" style="width:110px;height:9px"></span><span class="calc__tick">✓</span></div>
      <span class="btn" style="font-size:4.5px;padding:3px 8px;margin:8px auto 0">Calculate</span>
    </div>
  </section>

  <section class="reviews" style="height:72px;padding-top:10px">
    <p class="section-label">Testimonials</p>
    <h2 class="heading" style="font-size:9px;margin-bottom:6px">What Our Client Say?</h2>
    <div class="review" style="gap:6px">
      <div class="review__avatar" style="width:20px;height:20px" role="img" aria-label="Customer portrait"></div>
      <p class="review__quote text" style="width:150px;padding:3px 5px">Fast delivery, great soil and a crew that shows up on time. Highly recommended. — Mark D.</p>
    </div>
  </section>

  <section class="contact photo--forest" style="height:192px" role="img" aria-label="Background photo of a dark green forest">
    <div class="contact__card" style="width:220px;height:110px">
      <div class="contact__info" style="width:80px;padding:10px 8px">
        <h2 class="heading heading--light" style="font-size:8px;margin-bottom:5px">Get In Touch</h2>
        <p style="font-size:4px;line-height:1.8">(555) 014-7720<br>info@hollowbrookloam.com<br>Alder Ridge, ST<br>Licensed &amp; Insured</p>
      </div>
      <div class="contact__map" role="img" aria-label="Map showing the yard location"></div>
    </div>
    <div class="contact__form" style="width:220px;height:30px;margin-top:8px;padding:0 8px;gap:4px">
      <span style="font-size:5px;color:#fff;font-weight:600;white-space:nowrap">Message Us</span>
      <span class="input" style="flex:1;height:8px"></span><span class="input" style="flex:1;height:8px"></span>
      <span class="btn" style="font-size:4px;padding:2px 5px">Send</span>
    </div>
  </section>

  <footer class="footer">
    <div class="footer__cols" style="padding:12px 20px;gap:24px">
      <div class="footer__col"><h4>About</h4><p>Topsoil, mulch and<br>excavation since 1988.</p></div>
      <div class="footer__col"><h4>Services</h4><p>Excavation<br>Clearing<br>Grading</p></div>
      <div class="footer__col"><h4>Products</h4><p>Topsoil<br>Mulch<br>Compost</p></div>
      <div class="footer__col"><h4>Contact</h4><p>(555) 014-7720<br>Alder Ridge, ST</p></div>
    </div>
    <p class="footer__base" style="padding:4px">© 2024 Hollowbrook Loam. All rights reserved.</p>
  </footer>
</main>

<!-- ===== TABLET ===== -->
<main class="screen screen--tablet">
  <header class="nav" style="height:18px">
    <span class="brand" style="font-size:5px"><span class="brand__dot"></span>Hollowbrook Loam</span>
    <span class="btn" style="font-size:4px;padding:3px 4px">Get A Quote</span>
  </header>

  <section class="hero" style="height:118px;padding:0 20px;align-items:center;text-align:center" role="img" aria-label="Photo of fresh topsoil and young plants in garden beds">
    <div class="hero__body">
      <p class="hero__eyebrow">Welcome To Hollowbrook Loam</p>
      <h1 class="hero__title" style="font-size:11px">Providing Quality Topsoil<br>And Mulch Since 1988</h1>
      <span class="btn" style="font-size:4px;padding:3px 6px;margin-top:5px">Read More</span>
    </div>
  </section>

  <section class="features" style="height:34px;padding:0 6px">
    <div class="feature"><span class="feature__icon" style="width:12px;height:12px"></span>Topsoil</div>
    <div class="feature"><span class="feature__icon" style="width:12px;height:12px"></span>Mulch</div>
    <div class="feature"><span class="feature__icon" style="width:12px;height:12px"></span>Compost</div>
    <div class="feature"><span class="feature__icon" style="width:12px;height:12px"></span>Excavation</div>
    <div class="feature"><span class="feature__icon" style="width:12px;height:12px"></span>Clearing</div>
  </section>

  <section class="welcome" style="height:140px;flex-direction:column;justify-content:center;padding:0 20px;gap:6px">
    <div style="align-self:flex-start">
      <p class="section-label">About Us</p>
      <h2 class="heading" style="font-size:8px">Welcome To Hollowbrook Loam</h2>
    </div>
    <div style="display:flex;gap:10px;align-items:center">
      <p class="text" style="flex:1">Family owned for decades, we make and deliver topsoil, mulch and compost across the region.</p>
      <div class="photo photo--garden" style="width:110px;height:70px" role="img" aria-label="Photo of hands holding rich dark soil"></div>
    </div>
  </section>

  <section class="services" style="height:120px;padding:12px 10px 0">
    <p class="section-label">Our Services</p>
    <h2 class="heading" style="font-size:8px;margin-bottom:7px">How We Serve You</h2>
    <div class="service-grid" style="gap:5px">
      <article style="width:48px"><div class="photo photo--machine" style="height:38px" role="img" aria-label="Photo of an excavator"></div><span class="btn service-btn">Excavation</span></article>
      <article style="width:48px"><div class="photo photo--soil" style="height:38px" role="img" aria-label="Photo of topsoil"></div><span class="btn service-btn">Topsoil</span></article>
      <article style="width:48px"><div class="photo photo--forest" style="height:38px" role="img" aria-label="Photo of land clearing"></div><span class="btn service-btn">Clearing</span></article>
      <article style="width:48px"><div class="photo photo--machine" style="height:38px" role="img" aria-label="Photo of site grading"></div><span class="btn service-btn">Grading</span></article>
    </div>
  </section>

  <section class="calc" style="height:196px;padding-top:14px">
    <h2 class="heading heading--light" style="font-size:8px;margin-bottom:8px">How Much Do I Need?</h2>
    <div class="calc__panel" style="width:180px;padding:8px 10px">
      <div class="calc__row" style="height:20px"><span>Material</span><span class="calc__field" style="width:80px;height:8px"></span><span class="calc__tick">✓</span></div>
      <div class="calc__row" style="height:20px"><span>Length (ft)</span><span class="calc__field" style="width:80px;height:8px"></span><span class="calc__tick">✓</span></div>
      <div class="calc__row" style="height:20px"><span>Width (ft)</span><span class="calc__field" style="width:80px;height:8px"></span><span class="calc__tick">✓</span></div>
      <div class="calc__row" style="height:20px"><span>Depth (in)</span><span class="calc__field" style="width:80px;height:8px"></span><span class="calc__tick">✓</span></div>
      <div class="calc__row" style="height:20px"><span>Cubic Yards</span><span class="calc__field" style="width:80px;height:8px"></span><span class="calc__tick">✓</span></div>
      <span class="btn" style="font-size:4px;padding:3px 8px;margin:6px auto 0">Calculate</span>
    </div>
  </section>

  <section class="reviews" style="height:76px;padding-top:10px">
    <h2 class="heading" style="font-size:8px;margin-bottom:6px">What Our Client Say?</h2>
    <div class="review" style="gap:5px">
      <div class="review__avatar" style="width:18px;height:18px" role="img" aria-label="Customer portrait"></div>
      <p class="review__quote text" style="width:140px;padding:3px 5px">Fast delivery, great soil and a crew that shows up on time. — Mark D.</p>
    </div>
  </section>

  <section class="contact photo--forest" style="height:200px" role="img" aria-label="Background photo of a dark green forest">
    <div class="contact__card" style="width:180px;height:110px">
      <div class="contact__info" style="width:66px;padding:8px 6px">
        <h2 class="heading heading--light" style="font-size:7px;margin-bottom:4px">Get In Touch</h2>
        <p style="font-size:3.8px;line-height:1.8">(555) 014-7720<br>Alder Ridge, ST<br>Licensed &amp; Insured</p>
      </div>
      <div class="contact__map" role="img" aria-label="Map showing the yard location"></div>
    </div>
    <div class="contact__form" style="width:180px;height:28px;margin-top:8px;padding:0 6px;gap:4px">
      <span style="font-size:4.5px;color:#fff;font-weight:600;white-space:nowrap">Message Us</span>
      <span class="input" style="flex:1;height:7px"></span>
      <span class="btn" style="font-size:4px;padding:2px 4px">Send</span>
    </div>
  </section>

  <footer class="footer">
    <div class="footer__cols" style="padding:10px 14px;gap:14px">
      <div class="footer__col"><h4>Services</h4><p>Excavation<br>Clearing<br>Grading</p></div>
      <div class="footer__col"><h4>Products</h4><p>Topsoil<br>Mulch<br>Compost</p></div>
      <div class="footer__col"><h4>Contact</h4><p>(555) 014-7720<br>Alder Ridge, ST</p></div>
    </div>
    <p class="footer__base" style="padding:4px">© 2024 Hollowbrook Loam.</p>
  </footer>
</main>

<!-- ===== MOBILE ===== -->
<main class="screen screen--mobile">
  <header class="nav" style="height:16px;padding:0 4px">
    <span class="brand" style="font-size:3.6px">Hollowbrook Loam</span>
    <svg width="7" height="6" viewBox="0 0 7 6" aria-hidden="true"><rect y="0" width="7" height="1" fill="#b5121b"/><rect y="2.5" width="7" height="1" fill="#b5121b"/><rect y="5" width="7" height="1" fill="#b5121b"/></svg>
  </header>

  <section class="hero" style="height:70px;padding:0 6px;text-align:center" role="img" aria-label="Photo of fresh topsoil and young plants">
    <div class="hero__body"><h1 class="hero__title" style="font-size:5.5px">Providing Quality Topsoil And Mulch Since 1988</h1></div>
  </section>

  <section class="features" style="height:130px;flex-direction:column;justify-content:space-evenly">
    <div class="feature"><span class="feature__icon" style="width:11px;height:11px"></span>Topsoil</div>
    <div class="feature"><span class="feature__icon" style="width:11px;height:11px"></span>Mulch</div>
    <div class="feature"><span class="feature__icon" style="width:11px;height:11px"></span>Compost</div>
    <div class="feature"><span class="feature__icon" style="width:11px;height:11px"></span>Excavation</div>
  </section>

  <section class="welcome" style="height:96px;flex-direction:column;justify-content:center;padding:0 6px;gap:4px">
    <h2 class="heading" style="font-size:5px;text-align:center">Welcome To Hollowbrook Loam</h2>
    <div class="photo photo--garden" style="width:80px;height:44px" role="img" aria-label="Photo of hands holding rich dark soil"></div>
    <p class="text" style="font-size:3.5px;text-align:center">Soil, mulch and compost for every yard.</p>
  </section>

  <section class="services" style="height:220px;padding:8px 8px 0;display:flex;flex-direction:column;align-items:center;gap:5px">
    <h2 class="heading" style="font-size:5px">How We Serve You</h2>
    <div class="photo photo--machine" style="width:78px;height:38px" role="img" aria-label="Photo of an excavator"></div>
    <span class="btn" style="font-size:3.5px;padding:2px 6px">Excavation</span>
    <div class="photo photo--soil" style="width:78px;height:38px" role="img" aria-label="Photo of topsoil"></div>
    <span class="btn" style="font-size:3.5px;padding:2px 6px">Topsoil</span>
    <div class="photo photo--forest" style="width:78px;height:38px" role="img" aria-label="Photo of land clearing"></div>
    <span class="btn" style="font-size:3.5px;padding:2px 6px">Clearing</span>
  </section>

  <section class="calc" style="height:140px;padding-top:8px">
    <h2 class="heading heading--light" style="font-size:5px;margin-bottom:5px">How Much Do I Need?</h2>
    <div class="calc__panel" style="width:80px;padding:5px">
      <div class="calc__row" style="height:18px;font-size:3.5px"><span>Length</span><span class="calc__field" style="width:34px;height:6px"></span></div>
      <div class="calc__row" style="height:18px;font-size:3.5px"><span>Width</span><span class="calc__field" style="width:34px;height:6px"></span></div>
      <div class="calc__row" style="height:18px;font-size:3.5px"><span>Depth</span><span class="calc__field" style="width:34px;height:6px"></span></div>
      <div class="calc__row" style="height:18px;font-size:3.5px"><span>Yards</span><span class="calc__field" style="width:34px;height:6px"></span></div>
      <span class="btn" style="font-size:3.5px;padding:2px 5px;margin:5px auto 0">Calculate</span>
    </div>
  </section>

  <section class="reviews" style="height:70px;padding:8px 6px 0;gap:4px">
    <h2 class="heading" style="font-size:5px">What Our Client Say?</h2>
    <div class="review__avatar" style="width:14px;height:14px" role="img" aria-label="Customer portrait"></div>
    <p class="review__quote text" style="font-size:3.4px;padding:2px 4px;white-space:nowrap">Great soil, on time.</p>
  </section>

  <section class="contact photo--forest" style="height:190px;gap:6px" role="img" aria-label="Background photo of a dark green forest">
    <div class="contact__card" style="width:80px;height:110px;flex-direction:column">
      <div class="contact__info" style="padding:6px 5px">
        <h2 class="heading heading--light" style="font-size:5px;margin-bottom:3px">Get In Touch</h2>
        <p style="font-size:3.4px;line-height:1.7">(555) 014-7720<br>Alder Ridge, ST</p>
      </div>
      <div class="contact__map" role="img" aria-label="Map showing the yard location"></div>
    </div>
    <div class="contact__form" style="width:80px;height:40px;flex-direction:column;justify-content:center;gap:3px">
      <span class="input" style="width:64px;height:6px"></span><span class="input" style="width:64px;height:6px"></span>
      <span class="btn" style="font-size:3.4px;padding:2px 5px">Send</span>
    </div>
  </section>

  <footer class="footer">
    <div class="footer__cols" style="flex-direction:column;padding:8px 8px;gap:5px">
      <div class="footer__col"><h4 style="font-size:4px">Services</h4><p style="font-size:3.4px">Excavation · Grading</p></div>
      <div class="footer__col"><h4 style="font-size:4px">Products</h4><p style="font-size:3.4px">Topsoil · Mulch</p></div>
    </div>
    <p class="footer__base" style="padding:3px;font-size:3.2px">© 2024 Hollowbrook Loam</p>
  </footer>
</main>

</body>
</html>
```